NEW Escape Room. Fun, Dark and Mysterious.

Escape Room Website. Bookings and scheduling of appointments will be organised with Bookvane through the site. Most appointments will be created online through the booking system with some payments coming through in person by drop-ins. Groups will be from 2 - 8 people with a sliding scale of prices. We will start with one game playable and one saying coming soon. We will also eventually have 4 games up and running at once so will need it to be able to expand. We don't have any images of the rooms because it all relies heavily on mystery. Appointments are each 1 hour long with 30 minutes in between.

Target Market(s)

15-35 year olds

Coding

Coded - Design and coding required

Number of Pages Required

5+ page

Font styles to use
Decorative

Colors

Designer to choose colors to be used in the design.

Requirements
Must have
• Graphics showing what an escape room is.
• Page for About - What is an escape room
• Page for Games - Showing each of the different games which can be played with links to booking page. We have one game to start - the surgeons shadows. A victorian doctors office and serial killers. Then a game coming soon which is aztec/mayan/jungle/harold Crane feel.
• FAQ Page
Nice to have
• Graphics for multiple players ie 2 players, 3 players, 4 players etc
• Dark and Mysterious feel.
• Inspiration from Puzzle Vault, Cipher Lodge, Quest Lockbox
Should not have
• Cartoony/childish. Pink.
• Not bloody or dripping letters etc - not cliche.
• Not horror themed.

```html
<!DOCTYPE html>
<html lang="en">
<head>
<meta charset="utf-8">
<title>Lockhollow – Games</title>
<link href="https://fonts.googleapis.com/css2?family=Exo+2:wght@600;700;800&family=Catamaran:wght@400;500&display=swap" rel="stylesheet">
<style>
  :root {
    --bg: #000000;
    --header: #07121a;
    --amber: #fcab00;
    --white: #ffffff;
    --rule: #2a2a2a;
    --heading: "Exo 2", sans-serif;
    --body: "Catamaran", sans-serif;
  }
  * { margin: 0; padding: 0; box-sizing: border-box; }
  html, body { width: 1020px; height: 1200px; overflow: hidden; background: var(--bg); }
  body { position: relative; color: var(--white); font-family: var(--body); }
  a { color: inherit; text-decoration: none; }

  .site-header { position: absolute; left: 0; top: 0; width: 1020px; height: 57px; background: var(--header); }
  .main-nav a { position: absolute; top: 21px; font: 700 9.5px/14px var(--heading); letter-spacing: .1px; }
  .main-nav .is-active { color: var(--amber); }
  .header-phone { position: absolute; left: 675px; top: 21px; display: flex; align-items: center; gap: 7px; font: 700 11px/14px var(--heading); letter-spacing: .3px; }
  .header-book { position: absolute; left: 784px; top: 14px; width: 108px; height: 29px; background: var(--amber); color: #1a1200; font: 700 11px/29px var(--heading); text-align: center; }

  .page-banner { position: absolute; left: 103px; top: 57px; width: 759px; height: 148px;
    background:
      radial-gradient(ellipse 60px 80px at 85px 75px, rgba(120,95,55,.55), transparent 70%),
      radial-gradient(ellipse 190px 70px at 230px 100px, rgba(150,110,70,.65), transparent 75%),
      radial-gradient(ellipse 90px 85px at 635px 70px, rgba(110,75,40,.7), transparent 75%),
      radial-gradient(ellipse 170px 90px at 560px 110px, rgba(95,65,30,.55), transparent 80%),
      radial-gradient(ellipse 30px 70px at 730px 80px, rgba(120,110,90,.45), transparent 75%),
      linear-gradient(90deg, #060504 0%, #1b140d 18%, #2a1e12 40%, #1a130b 55%, #2e2012 80%, #120d08 100%); }
  .banner-title { position: absolute; left: 653px; top: 112px; font: 700 33px/38px var(--heading); color: var(--amber); }

  .brand { position: absolute; left: 456px; top: 12px; width: 120px; display: flex; flex-direction: column; align-items: center; gap: 8px; }
  .brand-mark { width: 52px; height: 52px; border-radius: 50%; background: var(--amber); }
  .brand-name { font: 700 19px/22px var(--heading); color: var(--amber); }

  .section-title { position: absolute; left: 0; width: 1020px; top: 251px; text-align: center; font: 800 20px/26px var(--heading); }

  .game-image { position: absolute; top: 317px; width: 370px; height: 279px; border: 1px solid #3a2a18; }
  .game-image--surgeon { left: 128px; background: radial-gradient(ellipse 150px 130px at 45% 42%, #c4101a 0%, #7a0609 40%, #2a0406 75%, #0d0203 100%); }
  .game-image--tomb { left: 523px; border-color: #3a3550; background: radial-gradient(ellipse 220px 170px at 55% 55%, #5a2c78 0%, #3d2660 40%, #231e40 75%, #16152c 100%); }

  .game-card-text { position: absolute; width: 370px; text-align: center; }
  .game-name { position: absolute; top: 618px; font: 700 13.5px/18px var(--heading); }
  .game-tagline { position: absolute; top: 640px; font: 400 10px/14px var(--body); letter-spacing: .2px; }
  .difficulty { position: absolute; top: 680px; display: flex; align-items: center; gap: 10px; }
  .difficulty-label { font: 700 8px/10px var(--heading); letter-spacing: .4px; }
  .difficulty-stars { display: flex; gap: 4.5px; }
  .game-summary { position: absolute; top: 710px; padding: 0 3px; font: 400 11.4px/19px var(--body); }
  .btn-book { position: absolute; top: 814px; left: 128px; width: 370px; height: 29px; background: var(--amber); color: #1a1200; font: 700 11px/29px var(--heading); text-align: center; border-radius: 1px; }
  .btn-soon { position: absolute; top: 814px; left: 521px; width: 370px; height: 29px; border: 2px solid var(--amber); color: var(--amber); font: 700 11px/25px var(--heading); text-align: center; border-radius: 1px; }

  .hours { position: absolute; left: 0; width: 1020px; top: 888px; text-align: center; font: 700 15.8px/31px var(--heading); letter-spacing: -.1px; }
  .hours em { font-style: normal; color: var(--amber); }

  .site-footer { position: absolute; left: 0; top: 1066px; width: 1020px; height: 134px; border-top: 1px solid var(--amber); }
  .social-links { position: absolute; top: 29px; left: 467px; display: flex; gap: 7.5px; }
  .social-links span { width: 14px; height: 14px; border-radius: 50%; background: var(--white); box-shadow: inset 0 0 0 4px var(--white), inset 0 0 0 6px #000; }
  .footer-nav { position: absolute; top: 65px; left: 0; width: 1020px; display: flex; justify-content: center; gap: 14px; font: 700 9.5px/14px var(--heading); }
  .footer-nav i { font-style: normal; }
  .footer-bottom { position: absolute; top: 100px; left: 0; width: 1020px; border-top: 1px solid var(--rule); }
  .copyright { position: absolute; left: 159px; top: 11px; font: 500 8px/12px var(--body); letter-spacing: .2px; white-space: nowrap; }
  .legal-links { position: absolute; left: 736px; top: 11px; font: 500 8px/12px var(--body); letter-spacing: .2px; white-space: nowrap; }
</style>
</head>
<body>
<svg width="0" height="0" style="position:absolute">
  <defs>
    <symbol id="star" viewBox="0 0 24 24"><path d="M12 1.5l3.1 6.9 7.4.7-5.6 5 1.7 7.4L12 17.6 5.4 21.5l1.7-7.4-5.6-5 7.4-.7z"/></symbol>
    <linearGradient id="half"><stop offset="50%" stop-color="#fcab00"/><stop offset="50%" stop-color="transparent"/></linearGradient>
  </defs>
</svg>

<header class="site-header">
  <nav class="main-nav">
    <a style="left:126px">HOME</a>
    <a style="left:191px">ABOUT US</a>
    <a class="is-active" style="left:274px">GAMES</a>
    <a style="left:344px">CONTACT US</a>
    <a style="left:437px">FAQ</a>
  </nav>
  <div class="header-phone">
    <svg width="11" height="11" viewBox="0 0 24 24" fill="none" stroke="#fff" stroke-width="1.8"><path d="M5 2h4l2 5-2.5 1.5a11 11 0 0 0 7 7L17 13l5 2v4a2 2 0 0 1-2 2A18 18 0 0 1 3 4a2 2 0 0 1 2-2z"/></svg>
    000-000-000
  </div>
  <a class="header-book">BOOK NOW</a>
</header>

<div class="page-banner" role="img" aria-label="Dim study scene with an hourglass, stacked old books, an antique clock and a candle"></div>
<div class="banner-title">Games</div>

<div class="brand"><span class="brand-mark"></span><span class="brand-name">Lockhollow</span></div>

<h1 class="section-title">GAMES</h1>

<div class="game-image game-image--surgeon" role="img" aria-label="Hooded figure from behind facing a large stethoscope in red smoke"></div>
<div class="game-image game-image--tomb" role="img" aria-label="Ancient jungle temple ruin overgrown with tree roots in purple light"></div>

<div class="game-card-text game-name" style="left:128px">The Surgeons Shadows</div>
<div class="game-card-text game-tagline" style="left:128px">The Doctor Will See You Now</div>
<div class="difficulty" style="left:136px">
  <span class="difficulty-label">DIFFICULTY LEVEL :</span>
  <span class="difficulty-stars">
    <svg width="14" height="14" fill="#fcab00"><use href="#star"/></svg>
    <svg width="14" height="14" fill="#fcab00"><use href="#star"/></svg>
    <svg width="14" height="14" fill="#fcab00"><use href="#star"/></svg>
    <svg width="14" height="14" fill="#fcab00"><use href="#star"/></svg>
    <svg width="14" height="14" fill="none" stroke="#fcab00" stroke-width="1.5" viewBox="0 0 24 24"><path d="M12 1.5l3.1 6.9 7.4.7-5.6 5 1.7 7.4L12 17.6 5.4 21.5l1.7-7.4-5.6-5 7.4-.7z"/></svg>
  </span>
</div>
<p class="game-card-text game-summary" style="left:128px">Paris in the winter of 1822. The nights are long and unseasonably cold. The streets are dark and uncharacteristically quiet. But for the latter there is a truth shrouded in fear that keeps the populous from venturing after dark. Every week icy sheets of blood gleen the streets of Paris at dawn...</p>
<a class="btn-book">BOOK NOW</a>

<div class="game-card-text game-name" style="left:520px">Serpent’s Tomb</div>
<div class="game-card-text game-tagline" style="left:521px">Coming Soon</div>
<div class="difficulty" style="left:528px">
  <span class="difficulty-label">DIFFICULTY LEVEL :</span>
  <span class="difficulty-stars">
    <svg width="14" height="14" fill="#fcab00"><use href="#star"/></svg>
    <svg width="14" height="14" fill="#fcab00"><use href="#star"/></svg>
    <svg width="14" height="14" fill="#fcab00"><use href="#star"/></svg>
    <svg width="14" height="14" viewBox="0 0 24 24" fill="url(#half)" stroke="#fcab00" stroke-width="1.5"><path d="M12 1.5l3.1 6.9 7.4.7-5.6 5 1.7 7.4L12 17.6 5.4 21.5l1.7-7.4-5.6-5 7.4-.7z"/></svg>
    <svg width="14" height="14" fill="none" stroke="#fcab00" stroke-width="1.5" viewBox="0 0 24 24"><path d="M12 1.5l3.1 6.9 7.4.7-5.6 5 1.7 7.4L12 17.6 5.4 21.5l1.7-7.4-5.6-5 7.4-.7z"/></svg>
  </span>
</div>
<p class="game-card-text game-summary" style="left:521px">Lorem ipsum dolor sit amet, consectetur adipiscing elit, sed do eiusmod tempor incididunt ut labore et dolore magna aliqua. Ut enim ad minim veniam, quis nostrud exercitation ullamco laboris nisi ut aliquip ex ea commodo esse cillum dolore eu fugiat t laborum...</p>
<a class="btn-soon">COMING SOON</a>

<div class="hours">
  Business is open by appointment.<br>
  Hours start from <em>8am</em> to last game at <em>9pm</em>.<br>
  Blocks are 60 minutes with 30 minutes between each appointment.
</div>

<footer class="site-footer">
  <div class="social-links"><span></span><span></span><span></span><span></span></div>
  <nav class="footer-nav">
    <a>HOME</a><i>|</i><a>ABOUT US</a><i>|</i><a>GAMES</a><i>|</i><a>CONTACT US</a><i>|</i><a>FAQ</a>
  </nav>
  <div class="footer-bottom">
    <div class="copyright">Copyright © 2020 Lockhollow. &nbsp;&nbsp;&nbsp;All Rights Reserved.</div>
    <div class="legal-links">Terms of Use &nbsp;&nbsp;&nbsp; | &nbsp;&nbsp;&nbsp;Privacy Policy</div>
  </div>
</footer>
</body>
</html>
```